File Download Website

We are looking for a design for a file download website. Our objective is to allow users to upload/browse/download files. This means we need 3 different pages.
The upload page should allow users to upload a file, we are looking for creative designs, a file box with a browse button next to it is already out there so the design must bring something new.
The browse page should display a users files/folders.
The download page should allow the user to download a file.
We do not require any code, only design. The designer is given complete freedom over the design, you may go about it however you like. This is a test of creativity, whoever this project goes to will definitely be given more work in the near future.
Example of a well designed file download website: cloudvane.net
Target Market(s)
15-30 year old people
Industry/Entity Type
Work
Look and feel
Each slider illustrates characteristics of the customer's brand and the style your logo design should communicate.

```html
<!DOCTYPE html>
<html lang="en">
<head>
<meta charset="utf-8">
<title>DataKeep – Download</title>
<link rel="stylesheet" href="https://fonts.googleapis.com/css2?family=Lato:wght@400;700;900&family=Arimo:wght@700&display=swap">
<style>
  :root {
    --header-top: #1ec0e6;
    --header-bottom: #0e97cf;
    --body-top: #e8f5fc;
    --body-mid: #a3d7ec;
    --body-bottom: #1096cf;
    --brand-ink: #2a2a2a;
    --nav-face-top: #fafafa;
    --nav-face-bottom: #dcdcdc;
    --nav-active-top: #c8c8c8;
    --nav-active-bottom: #b0b0b0;
    --nav-text: #b9b9b9;
    --nav-active-text: #9a9a9a;
    --rule-edge: #25b6d8;
    --rule-core: #0b3e55;
    --title-ink: #555a5e;
    --panel: #f1f1f1;
    --button-top: #f6f6f6;
    --button-bottom: #dedede;
    --action-blue: #4671a6;
    --footer-ink: #1d4d68;
  }
  * { box-sizing: border-box; margin: 0; padding: 0; }
  html, body { width: 1200px; height: 840px; overflow: hidden; }
  body { font-family: "Lato", sans-serif; }

  .page {
    position: relative;
    width: 1200px;
    height: 840px;
    background: linear-gradient(to bottom, var(--body-top) 127px, var(--body-mid) 430px, var(--body-bottom) 840px);
  }

  .site-header {
    position: absolute; left: 0; top: 0;
    width: 1200px; height: 127px;
    background: linear-gradient(to bottom, var(--header-top), var(--header-bottom));
  }
  .brand {
    position: absolute; left: 22px; top: 4px;
    font-size: 84px; font-weight: 700; letter-spacing: -1px;
    color: var(--brand-ink);
    line-height: 1;
  }

  .main-nav { position: absolute; top: 22px; left: 600px; display: flex; gap: 7px; }
  .nav-item {
    width: 192px; height: 60px;
    display: flex; align-items: center; justify-content: center;
    border-radius: 3px;
    background: linear-gradient(to bottom, var(--nav-face-top), var(--nav-face-bottom));
    box-shadow: 0 8px 6px -4px rgba(0,0,0,0.35);
    color: var(--nav-text);
    font-size: 25px; font-weight: 700;
    text-shadow: 0 1px 0 #fff;
    text-decoration: none;
  }
  .nav-item.is-active {
    background: linear-gradient(to bottom, var(--nav-active-top), var(--nav-active-bottom));
    color: var(--nav-active-text);
    text-shadow: 0 1px 0 #ddd;
  }

  .rule {
    position: absolute; left: 235px; width: 749px; height: 3px;
    background: linear-gradient(to right, var(--rule-edge), var(--rule-core) 50%, var(--rule-edge));
  }
  .rule-top { top: 423px; }
  .rule-bottom { top: 507px; }

  .file-title {
    position: absolute; left: 0; top: 440px; width: 1200px;
    text-align: center;
    font-size: 44px; font-weight: 400;
    color: var(--title-ink);
    text-shadow: 0 2px 2px rgba(255,255,255,0.9);
  }

  .download-panel {
    position: absolute; left: 340px; top: 524px;
    width: 540px; height: 144px;
    border-radius: 9px;
    background: var(--panel);
  }
  .download-button {
    position: absolute; left: 33px; top: 33px;
    width: 472px; height: 81px;
    border-radius: 8px;
    background: linear-gradient(to bottom, var(--button-top), var(--button-bottom));
    box-shadow: 0 2px 3px rgba(0,0,0,0.3), inset 0 1px 0 #fff;
    display: flex; align-items: center;
    text-decoration: none;
  }
  .download-label {
    margin-left: 53px;
    font-family: "Arimo", sans-serif;
    font-weight: 700; font-size: 37px;
    color: var(--action-blue);
  }
  .download-icon { position: absolute; left: 322px; top: 15px; }

  .site-footer {
    position: absolute; left: 0; top: 781px; width: 1200px;
    text-align: center; font-size: 17px; color: var(--footer-ink);
  }
</style>
</head>
<body>
<div class="page">
  <header class="site-header">
    <div class="brand">DataKeep</div>
    <nav class="main-nav">
      <a class="nav-item" href="#">UPLOAD</a>
      <a class="nav-item" href="#">BROWSE</a>
      <a class="nav-item is-active" href="#">DOWNLOAD</a>
    </nav>
  </header>

  <main>
    <div class="rule rule-top"></div>
    <h1 class="file-title">Download Your File Name. PDF</h1>
    <div class="rule rule-bottom"></div>

    <div class="download-panel">
      <a class="download-button" href="#">
        <span class="download-label">DOWNLOAD</span>
        <svg class="download-icon" width="86" height="54" viewBox="0 0 86 54" aria-hidden="true">
          <path d="M14 52 C4 52 0 44 2 38 C4 31 11 29 16 30 C16 18 26 12 35 14 C40 4 54 2 62 10 C67 15 67 22 66 26 C76 25 84 32 84 40 C84 47 79 52 72 52 Z" fill="var(--action-blue)"/>
          <rect x="38" y="22" width="10" height="16" fill="#fff"/>
          <path d="M31 36 L55 36 L43 50 Z" fill="#fff"/>
        </svg>
      </a>
    </div>
  </main>

  <footer class="site-footer">Copyright@datakeep.net</footer>
</div>
</body>
</html>
```